Professional Home Buyer business card needed

I need a pretty straight forward business card designed. We help people that NEED to sell their homes solve problems. We perform all types of Real Estate transactions including flip, wholesale, investment, rental property and multi family. The card will mainly be used to give to prospective Sellers but will also be given to Real Estate Investors as well. It should professional and very easy to read, most clients are older people.

Target Market(s)

Distressed home sellers as well as Real Estate investors

Industry/Entity Type

Real Estate

Contact Information for Business Card

should be a professional layout

Colors
ec1f27
ffffff
000000

Requirements
Must have
• Large logo on back and smaller one on front. should utilize Red, white, and black.
• I am thinking of using a soft touch coating on the card so keep that in mind.
• Contact info should be very easy to read, think older clients.
Nice to have
• I would like to see a design with rounded corners on the card
Should not have
• pictures of homes or other home graphics.

```html
<!DOCTYPE html>
<html lang="en">
<head>
<meta charset="utf-8">
<title>Keystead Home Buyers – Business Card</title>
<link href="https://fonts.googleapis.com/css2?family=Open+Sans:wght@700&family=PT+Sans+Narrow:wght@700&family=Saira:wght@600;800&display=swap" rel="stylesheet">
<style>
  :root {
    --stage: #949494;
    --red: #ec1f27;
    --red-dark: #9e1a1f;
    --black: #000000;
    --card-black: #0c0c0c;
    --white: #ffffff;
    --icon-grey: #3a3a3a;
    --icon-grey-light: #4a4a4a;
  }
  * { margin: 0; padding: 0; box-sizing: border-box; }
  html, body { width: 1200px; height: 1000px; overflow: hidden; }
  body { background: var(--stage); position: relative; font-family: "PT Sans Narrow", sans-serif; }

  .card {
    position: absolute; left: 213px; width: 775px; height: 443px;
    border-radius: 18px; overflow: hidden;
    box-shadow: 4px 5px 6px rgba(0,0,0,0.35);
  }
  .card--front { top: 38px; background: var(--white); }
  .card--back { top: 511px; background: var(--card-black); }

  .front-shapes { position: absolute; inset: 0; }

  .holder { position: absolute; left: 59px; top: 58px; }
  .holder__name { font-family: "Open Sans", sans-serif; font-weight: 700; font-size: 29px; color: var(--white); line-height: 1; letter-spacing: -0.3px; }
  .holder__title { font-family: "Open Sans", sans-serif; font-weight: 700; font-size: 20px; color: var(--red); letter-spacing: 3.2px; line-height: 1; margin-top: 3px; }
  .holder__rule { width: 71px; height: 2px; background: var(--white); margin-top: 8px; }

  .contact-list { position: absolute; left: 60px; top: 168px; list-style: none; }
  .contact-item { display: flex; align-items: center; height: 48px; margin-bottom: 9px; }
  .contact-icon {
    width: 47px; height: 48px; flex: none;
    background: linear-gradient(135deg, var(--icon-grey-light) 50%, var(--icon-grey) 50%);
    display: flex; align-items: center; justify-content: center;
  }
  .contact-icon--accent { background: linear-gradient(135deg, var(--red) 50%, #c81a21 50%); }
  .contact-text { color: var(--white); font-size: 21px; font-weight: 700; margin-left: 12px; line-height: 1.4; }

  .brand { position: absolute; text-align: center; }
  .brand__tagline { font-family: "Saira", sans-serif; font-weight: 600; letter-spacing: 3px; line-height: 1; white-space: nowrap; }
  .brand__name { font-family: "Saira", sans-serif; font-weight: 800; line-height: 1; display: flex; align-items: center; justify-content: center; gap: 12px; }
  .brand__mark { background: var(--red); flex: none; }
  .brand__sub { font-family: "Saira", sans-serif; font-weight: 800; line-height: 1; }

  .brand--front { left: 470px; top: 158px; width: 270px; }
  .brand--front .brand__tagline { font-size: 12px; color: var(--black); }
  .brand--front .brand__name { font-size: 44px; color: var(--black); margin-top: 24px; }
  .brand--front .brand__mark { width: 22px; height: 22px; }
  .brand--front .brand__sub { font-size: 19px; color: var(--black); letter-spacing: 3px; margin-top: 30px; }

  .back-map { position: absolute; left: 28px; top: 38px; width: 720px; height: 345px; }
  .back-rule { position: absolute; top: 219px; height: 4px; background: var(--red); }
  .back-rule--left { left: 0; width: 179px; }
  .back-rule--right { left: 595px; width: 180px; }

  .brand--back { left: 200px; top: 139px; width: 375px; }
  .brand--back .brand__tagline { font-size: 15px; color: var(--white); letter-spacing: 4px; }
  .brand--back .brand__name { font-size: 58px; color: var(--white); margin-top: 34px; }
  .brand--back .brand__mark { width: 28px; height: 28px; }
  .brand--back .brand__sub { font-size: 24px; color: var(--white); letter-spacing: 4px; margin-top: 40px; }
</style>
</head>
<body>

<section class="card card--front">
  <svg class="front-shapes" width="775" height="443" viewBox="0 0 775 443" aria-hidden="true">
    <path d="M0 0 H470 C458 170 420 330 345 443 H0 Z" fill="var(--red-dark)"/>
    <path d="M0 0 H432 C438 160 410 320 345 443 H0 Z" fill="var(--red)"/>
    <path d="M0 0 H344 C430 110 432 320 345 443 H0 Z" fill="var(--card-black)"/>
  </svg>

  <div class="holder">
    <p class="holder__name">Dana Whitfield</p>
    <p class="holder__title">President</p>
    <div class="holder__rule"></div>
  </div>

  <ul class="contact-list">
    <li class="contact-item">
      <span class="contact-icon contact-icon--accent">
        <svg width="16" height="28" viewBox="0 0 16 28" aria-hidden="true"><rect x="1" y="1" width="14" height="26" rx="2.5" fill="none" stroke="#fff" stroke-width="2"/><line x1="1" y1="21" x2="15" y2="21" stroke="#fff" stroke-width="1.5"/><circle cx="8" cy="24" r="1.2" fill="#fff"/></svg>
      </span>
      <span class="contact-text">555-014-2283</span>
    </li>
    <li class="contact-item">
      <span class="contact-icon">
        <svg width="28" height="20" viewBox="0 0 28 20" aria-hidden="true"><rect x="1" y="1" width="26" height="18" fill="none" stroke="#fff" stroke-width="2"/><path d="M1 1 L14 12 L27 1 M1 19 L11 9 M27 19 L17 9" fill="none" stroke="#fff" stroke-width="2"/></svg>
      </span>
      <span class="contact-text">dana@prairiehomeoffers.com</span>
    </li>
    <li class="contact-item">
      <span class="contact-icon">
        <svg width="28" height="28" viewBox="0 0 28 28" aria-hidden="true"><g fill="none" stroke="#fff" stroke-width="1.6"><circle cx="14" cy="14" r="12"/><ellipse cx="14" cy="14" rx="5.5" ry="12"/><line x1="2" y1="14" x2="26" y2="14"/><path d="M4 8 H24 M4 20 H24"/></g></svg>
      </span>
      <span class="contact-text">www.prairiehomeoffers.com</span>
    </li>
    <li class="contact-item">
      <span class="contact-icon">
        <svg width="20" height="28" viewBox="0 0 20 28" aria-hidden="true"><path d="M10 1 C4.5 1 1 5 1 10 C1 17 10 27 10 27 C10 27 19 17 19 10 C19 5 15.5 1 10 1 Z" fill="#fff"/><circle cx="10" cy="10" r="3.6" fill="var(--icon-grey)"/></svg>
      </span>
      <span class="contact-text">P.O. Box 210<br>Maple Ridge, KS 67999</span>
    </li>
  </ul>

  <div class="brand brand--front">
    <p class="brand__tagline">SELLING MADE SIMPLE!</p>
    <p class="brand__name"><span class="brand__mark"></span>KEYSTEAD</p>
    <p class="brand__sub">HOME BUYERS</p>
  </div>
</section>

<section class="card card--back">
  <svg class="back-map" viewBox="0 0 720 345" role="img" aria-label="Faint dotted world map in dark red tones">
    <defs>
      <radialGradient id="mapTone" cx="50%" cy="45%" r="60%">
        <stop offset="0%" stop-color="#2a0c0e"/>
        <stop offset="100%" stop-color="#0c0c0c"/>
      </radialGradient>
    </defs>
    <rect width="720" height="345" fill="url(#mapTone)"/>
  </svg>

  <div class="back-rule back-rule--left"></div>
  <div class="back-rule back-rule--right"></div>

  <div class="brand brand--back">
    <p class="brand__tagline">SELLING MADE SIMPLE!</p>
    <p class="brand__name"><span class="brand__mark"></span>KEYSTEAD</p>
    <p class="brand__sub">HOME BUYERS</p>
  </div>
</section>

</body>
</html>
```